harvest Ahead Book Cover Design for real estate investment book

I am looking for a Book Cover design for my new book. I would like designs for a hardcover, softcover and Lumora book.

The book deals with real estate and mortgage investments. Looking for a clean, bright simple design. Want to cover to be White with big RED letters. See "Leading from Wonder" book for an example ... see attached.

Target Market(s)

Affluent people with money looking for investment solutions.

Industry/Entity Type

Financial Service

Font styles to use
Serif

Requirements
Must have
• Bright clean design that will be appealing to affluent people.
• Title: harvest AHEAD
• Subtitle: The quiet path to thriving through property holdings
• subsubtitle: Secrets Your Fund Manager Keeps Quiet About...
• Author: Ned Garroway
• My Picture on the inside cover or on the back cover
• Book Description, Author description
Nice to have
• Focus on the Front cover look and feel first. Then we can look at the inside flaps and back cover. I will need to send you text. This is for the full cover. Front. Back. Spine. Inside flaps fro hardcover.

```html
<!DOCTYPE html>
<html lang="en">
<head>
<meta charset="utf-8">
<title>Harvest Ahead – Front Cover</title>
<link href="https://fonts.googleapis.com/css2?family=Anton&family=Roboto+Condensed:wght@600&family=Exo+2:wght@400;600&display=swap" rel="stylesheet">
<style>
  :root {
    --backdrop: #c9c9c9;
    --cover-white: #f7f7f7;
    --title-red: #d6000c;
    --ink: #161616;
    --box-text: #ffffff;
  }
  * { margin: 0; padding: 0; box-sizing: border-box; }
  html, body {
    width: 1200px;
    height: 1037px;
    overflow: hidden;
    background: var(--backdrop);
  }
  .stage {
    width: 1200px;
    height: 1037px;
    display: flex;
    align-items: center;
    justify-content: center;
  }
  .book-cover {
    width: 560px;
    height: 890px;
    background: var(--cover-white);
    padding: 40px 35px 36px;
    display: flex;
    flex-direction: column;
    align-items: center;
    box-shadow: 0 6px 24px rgba(0,0,0,0.18);
  }
  .title-word {
    display: block;
    width: 490px;
    fill: var(--title-red);
    font-family: "Anton", "Impact", sans-serif;
  }
  .subtitle {
    font-family: "Roboto Condensed", "Arial Narrow", sans-serif;
    font-weight: 600;
    font-size: 27px;
    line-height: 1.2;
    text-transform: uppercase;
    text-align: center;
    color: var(--ink);
    margin: 12px 0 18px;
    letter-spacing: -0.01em;
  }
  .tagline-box {
    width: 470px;
    background: var(--ink);
    color: var(--box-text);
    font-family: "Exo 2", sans-serif;
    font-weight: 400;
    font-size: 30px;
    line-height: 1.28;
    text-transform: uppercase;
    text-align: center;
    padding: 18px 24px;
    margin-top: 26px;
  }
  .author {
    margin-top: 22px;
    width: 470px;
    display: flex;
    justify-content: space-between;
    font-family: "Exo 2", sans-serif;
    font-weight: 600;
    font-size: 26px;
    color: var(--ink);
  }
</style>
</head>
<body>
  <main class="stage">
    <article class="book-cover">
      <svg class="title-word" viewBox="0 0 490 190" height="190" aria-label="Harvest">
        <text x="0" y="185" font-size="245" textLength="490" lengthAdjust="spacingAndGlyphs">HARVEST</text>
      </svg>
      <p class="subtitle">The quiet path to thriving<br>through property holdings</p>
      <svg class="title-word" viewBox="0 0 490 245" height="245" aria-label="Ahead">
        <text x="0" y="240" font-size="320" textLength="490" lengthAdjust="spacingAndGlyphs">AHEAD</text>
      </svg>
      <p class="tagline-box">Secrets your fund<br>manager keeps<br>quiet about...</p>
      <p class="author">
        <span>N</span><span>E</span><span>D</span><span>&nbsp;</span><span>G</span><span>A</span><span>R</span><span>R</span><span>O</span><span>W</span><span>A</span><span>Y</span>
      </p>
    </article>
  </main>
</body>
</html>
```